Postcard for manufacturing company

We make stainless steel essential oil extraction equipment for unique businesses in Washington and Oregon (USA). We are seeking a design for a mailer that will serve as our first contact with potential customers who operate businesses that require this type of equipment. We'd like a large form postcard that integrates the attached photo, along with a few key features. The back should be generic post card format and allow us to add our own sales pitch.
Sales text for front: "State Approved Cannabis Extraction Technology" "Safe - Affordable - Custom" "Specializing in Full Service Solutions" "Free Consultation" "1 855 730 DUNE (3863)"

```html
<!DOCTYPE html>
<html lang="en">
<head>
<meta charset="utf-8">
<title>Extraction Equipment Postcard</title>
<link href="https://fonts.googleapis.com/css2?family=Fira+Sans:wght@600;700;800&display=swap" rel="stylesheet">
<style>
  :root {
    --page: #ffffff;
    --ink: #111111;
    --yellow: #f6c31c;
    --white: #ffffff;
    --steel-light: #d9dbdc;
    --steel-mid: #9ea3a6;
    --steel-dark: #4b4f52;
    --card-edge: #c9c9c9;
    --rule: #9a9a9a;
    --stamp: #d6d6d6;
  }
  * { margin: 0; padding: 0; box-sizing: border-box; }
  html, body {
    width: 900px; height: 1200px; overflow: hidden;
    background: var(--page);
    font-family: "Fira Sans", Arial, sans-serif;
  }
  .canvas { position: relative; width: 900px; height: 1200px; }

  .postcard-front {
    position: absolute; left: 42px; top: 15px; width: 816px; height: 570px;
    overflow: hidden;
  }
  .equipment-photo {
    position: absolute; inset: 0;
    background:
      radial-gradient(ellipse at 30% 35%, var(--steel-light) 0%, transparent 45%),
      radial-gradient(ellipse at 75% 25%, #eef0f1 0%, transparent 40%),
      linear-gradient(180deg, var(--steel-mid) 0%, #b7babc 45%, #7d8285 75%, var(--steel-dark) 100%);
  }
  .tag {
    position: absolute; background: var(--yellow); color: var(--ink);
    font-weight: 700; white-space: nowrap; display: flex; align-items: center;
  }
  .tag-approval { right: 0; top: 21px; height: 36px; padding: 0 18px; font-size: 25px; }
  .tag-promise { left: 0; top: 69px; height: 48px; padding: 0 20px; font-size: 34px; font-weight: 800; }
  .tag-service { left: 0; top: 369px; height: 39px; padding: 0 18px; font-size: 27px; }
  .tag-consult { left: 0; top: 426px; height: 39px; padding: 0 18px; font-size: 27px; }
  .phone {
    position: absolute; left: 18px; top: 480px;
    color: var(--white); font-size: 42px; font-weight: 800; letter-spacing: 1px;
  }
  .brand {
    position: absolute; right: 24px; top: 400px;
    display: flex; align-items: center; gap: 10px;
    color: var(--white); font-size: 40px; font-weight: 800;
  }
  .brand-dot { width: 26px; height: 26px; border-radius: 50%; background: var(--white); }

  .postcard-back {
    position: absolute; left: 42px; top: 609px; width: 816px; height: 582px;
    border: 2px solid var(--card-edge); background: var(--white);
  }
  .divider {
    position: absolute; left: 406px; top: 48px; width: 2px; height: 495px;
    background: var(--rule);
  }
  .stamp-box {
    position: absolute; left: 672px; top: 55px; width: 90px; height: 93px;
    background: var(--stamp);
  }
  .address-lines { position: absolute; left: 432px; top: 235px; width: 342px; }
  .address-lines span {
    display: block; height: 2px; background: var(--rule); margin-bottom: 54px;
  }
</style>
</head>
<body>
<main class="canvas">
  <section class="postcard-front">
    <div class="equipment-photo" role="img" aria-label="Photo of stainless steel extraction equipment with pressure gauges and valves"></div>
    <div class="tag tag-approval">State Approved Cannabis Extraction Technology</div>
    <div class="tag tag-promise">Safe - Affordable - Custom</div>
    <div class="tag tag-service">Specializing in Full Service Solutions</div>
    <div class="tag tag-consult">Free Consultation</div>
    <div class="phone">1 855 730 DUNE (3863)</div>
    <div class="brand"><span class="brand-dot"></span>Cascadia</div>
  </section>

  <section class="postcard-back">
    <div class="divider"></div>
    <div class="stamp-box"></div>
    <div class="address-lines">
      <span></span><span></span><span></span><span></span><span></span>
    </div>
  </section>
</main>
</body>
</html>
```